A New and modern Business Card for Talvern Contract Partners Ltd

New and modern Logo and Business Card Attached is the current logo/business card designCurrently the business is called "Talvern & Co." or TCP Ltd for short. This is subject to change.This business specialises in Telecoms and Energy. We work with the major networks (KX, V7, etc) and also offer Energy Products saving clients money off their energy bills.These are business to business services.The current design incorporates a Pheonix, indicating rebirth, starting something new.We would like to maintain the Phoenix element but a newer modern style.We love colours in the logo 3 max.The aim of this is to be ultra slick and modern. I envisage Talvern & Co. on one side of the card with long descriptions on the other side.Side 1:TCP Ltd/Logo?Side 2:TCP Ltd/Logo/Graphic?Brogan & Co.Name:Address:Phone:Email:The design is mostly flexible but must incorporate a Phoenix.For example "Talvern & Co." with a block phoenix behind the text...up to you.

Industry/Entity Type

Telecommunications

Contact Information for Business Card

Talvern & Co.
Address:
Name:
Phone:
Email:

Logo Text

Talvern & Co.

Colors
33a6d7
0792cd
acd037
9bcb3c
f78f20
fece3e

Requirements
Must have
• Phoenix
• 3/4 colours max
• Blue representing Technology (wireless)
• Green for Eco Energy
• Orange for Phoenix
• White business card background
Should not have
• phoenix must not all be red/ orange fire, we are a technology service company and the phoenix colours must represent this. Fire is not representative of our company.

```html
<!DOCTYPE html>
<html lang="en">
<head>
<meta charset="utf-8">
<title>Talvern Contract Partners Limited – Business Card</title>
<link rel="stylesheet" href="https://fonts.googleapis.com/css2?family=Jost:wght@600;700&display=swap">
<style>
  :root {
    --card-white: #ffffff;
    --tech-blue: #0792cd;
    --tech-blue-light: #33a6d7;
    --eco-green: #9bcb3c;
    --phoenix-orange: #f78f20;
    --ink: #111111;
  }
  html, body {
    margin: 0;
    padding: 0;
    width: 1200px;
    height: 686px;
    overflow: hidden;
    background: var(--card-white);
  }
  .card {
    position: relative;
    width: 1200px;
    height: 686px;
    background: var(--card-white);
    font-family: "Jost", "Futura", sans-serif;
    overflow: hidden;
  }
  .brand-mark {
    position: absolute;
    top: 176px;
    left: 0;
    width: 1200px;
    height: 100px;
    display: flex;
    justify-content: center;
    align-items: center;
    gap: 24px;
  }
  .brand-mark__dot {
    width: 96px;
    height: 96px;
    border-radius: 50%;
    background: var(--phoenix-orange);
  }
  .brand-mark__name {
    font-weight: 700;
    font-size: 84px;
    line-height: 1;
    color: var(--ink);
    letter-spacing: 6px;
  }
  .company-name {
    position: absolute;
    top: 340px;
    left: 0;
    width: 1200px;
    margin: 0;
    text-align: center;
    font-weight: 700;
    font-size: 100px;
    line-height: 1;
    letter-spacing: 5px;
    color: var(--tech-blue);
  }
  .company-tagline {
    position: absolute;
    top: 452px;
    left: 0;
    width: 1200px;
    margin: 0;
    text-align: center;
    font-weight: 600;
    font-size: 40px;
    line-height: 1;
    letter-spacing: 0.5px;
    color: var(--ink);
  }
  .footer-rule {
    position: absolute;
    left: 0;
    top: 566px;
    width: 1200px;
    height: 14px;
    background: var(--eco-green);
  }
  .footer-band {
    position: absolute;
    left: 0;
    top: 580px;
    width: 1200px;
    height: 106px;
    background: var(--tech-blue);
  }
</style>
</head>
<body>
  <main class="card">
    <div class="brand-mark">
      <span class="brand-mark__dot"></span>
      <span class="brand-mark__name">TCP</span>
    </div>
    <h1 class="company-name">TALVERN</h1>
    <p class="company-tagline">Contract Partners Limited</p>
    <div class="footer-rule"></div>
    <div class="footer-band"></div>
  </main>
</body>
</html>
```